Label design for Bloody Mary mix

we are looking for a label design for a Bloody Mary mix we are making. we are calling it "Marlow's Ember"
thinking of maybe a farm girl pin up with a tattoo??
Open to all ideas
Thanks for your help!!!

Target Market(s)

Bloody Mary drinkers :)

Industry/Entity Type

Farm

Font styles to use
Serif
Sans Serif
Decorative
Script
Other font styles liked:
• any

Colors

Designer to choose colors to be used in the design.

```html
<!DOCTYPE html>
<html lang="en">
<head>
<meta charset="utf-8">
<title>Marlow's Ember — Premium Bloody Mary Mixxx Label</title>
<link rel="stylesheet" href="https://fonts.googleapis.com/css2?family=Kaushan+Script&family=Montserrat:wght@400;600;800&display=swap">
<style>
  :root {
    --page: #ffffff;
    --label-slate: #565656;
    --label-slate-frame: #c9241f;
    --label-red: #e30613;
    --label-red-frame: #ffffff;
    --ink-white: #ffffff;
    --ink-red: #e01b1b;
    --ink-dark: #1c1c1c;
  }
  html, body {
    margin: 0;
    width: 1200px;
    height: 999px;
    overflow: hidden;
    background: var(--page);
    font-family: "Montserrat", sans-serif;
  }
  .canvas {
    position: relative;
    width: 1200px;
    height: 999px;
  }
  .label {
    position: absolute;
    top: 505px;
    width: 262px;
    height: 300px;
  }
  .label--slate { left: 221px; }
  .label--red { left: 717px; }
  .label svg { display: block; overflow: visible; }

  .label__tagline {
    font-size: 9px;
    font-weight: 600;
    letter-spacing: 1.2px;
  }
  .label__name {
    font-family: "Kaushan Script", cursive;
    font-size: 46px;
    font-weight: 400;
  }
  .label__product {
    font-size: 10.5px;
    font-weight: 400;
    letter-spacing: 1.4px;
  }
  .label__product-accent { font-weight: 800; }
  .label__volume {
    font-size: 5px;
    font-weight: 600;
    letter-spacing: 0.6px;
  }

  .label--slate .label__base { fill: var(--label-slate); }
  .label--slate .label__frame { stroke: var(--label-slate-frame); }
  .label--slate .label__tagline { fill: var(--ink-red); }
  .label--slate .label__name { fill: var(--ink-red); }
  .label--slate .label__product { fill: var(--ink-white); }
  .label--slate .label__product-accent { fill: var(--ink-red); }
  .label--slate .label__volume { fill: var(--ink-dark); }

  .label--red .label__base { fill: var(--label-red); }
  .label--red .label__frame { stroke: var(--label-red-frame); }
  .label--red .label__tagline { fill: var(--ink-white); }
  .label--red .label__name { fill: var(--ink-white); }
  .label--red .label__product { fill: var(--ink-white); }
  .label--red .label__product-accent { fill: var(--ink-dark); }
  .label--red .label__volume { fill: var(--ink-dark); }
</style>
</head>
<body>
<main class="canvas">

  <section class="label label--slate">
    <svg width="262" height="300" viewBox="0 0 262 300">
      <defs>
        <linearGradient id="art-slate" x1="0" y1="0" x2="0" y2="1">
          <stop offset="0" stop-color="#3a3a3a"/>
          <stop offset="1" stop-color="#242424"/>
        </linearGradient>
      </defs>
      <path class="label__base" d="M0,14 Q131,-4 262,14 L262,284 Q131,302 0,284 Z"/>
      <path class="label__frame" fill="none" stroke-width="1" d="M7,20 Q131,4 255,20 L255,277 Q131,293 7,277 Z"/>
      <text class="label__tagline" x="131" y="26" text-anchor="middle">PREMIUM QUALITY</text>
      <rect x="42" y="42" width="178" height="112" rx="6" fill="url(#art-slate)" role="img" aria-label="Illustration of a farm girl in a wide hat and overalls holding a tomato, with a barn, tractor and fields behind her"/>
      <text class="label__name" x="128" y="192" text-anchor="middle">Marlow's</text>
      <text class="label__name" x="136" y="236" text-anchor="middle">Ember</text>
      <text class="label__product" x="131" y="261" text-anchor="middle">PREMIUM <tspan class="label__product-accent">BLOODY MARY</tspan> MIXXX</text>
      <text class="label__volume" x="131" y="279" text-anchor="middle">NET 32 FL OZ</text>
    </svg>
  </section>

  <section class="label label--red">
    <svg width="262" height="300" viewBox="0 0 262 300">
      <defs>
        <linearGradient id="art-red" x1="0" y1="0" x2="0" y2="1">
          <stop offset="0" stop-color="#3a1a1a"/>
          <stop offset="1" stop-color="#1f1f1f"/>
        </linearGradient>
      </defs>
      <path class="label__base" d="M0,14 Q131,-4 262,14 L262,284 Q131,302 0,284 Z"/>
      <path class="label__frame" fill="none" stroke-width="1" d="M7,20 Q131,4 255,20 L255,277 Q131,293 7,277 Z"/>
      <text class="label__tagline" x="131" y="26" text-anchor="middle">PREMUIM QUALITY</text>
      <rect x="42" y="42" width="178" height="112" rx="6" fill="url(#art-red)" role="img" aria-label="Illustration of a farm girl in a wide hat and overalls holding a tomato, with a barn, tractor and fields behind her"/>
      <text class="label__name" x="128" y="192" text-anchor="middle">Marlow's</text>
      <text class="label__name" x="136" y="236" text-anchor="middle">Ember</text>
      <text class="label__product" x="131" y="261" text-anchor="middle">PREMIUM <tspan class="label__product-accent">BLOODY MARY</tspan> MIXXX</text>
      <text class="label__volume" x="131" y="279" text-anchor="middle">NET 32 FL OZ</text>
    </svg>
  </section>

</main>
</body>
</html>
```